New company aimed at high net worth individuals needs a stationery design

We need a stationery design for a new company that is offering High Net Worth Individuals around the world a tailored giving service (enabling them to realise their personal aspirations in 'tailored giving'). Not looking for a logo because we think 'Tailored Giving...' speaks for itself. Looking for a clean look that smacks of (understated) quality and reliability to the billionaires who open our letters and folders.

Target Market(s)

High Net Worth Individuals, millionaires, CEOs of Companies, stock brokers, asset managers. Extremely wealthy individuals.

Industry/Entity Type

It Company

Contact Information for Business Card

Dr Gerald Finchley. Tailored Giving...
17 Corlett Road, Ludmere on Vane, Warwickshire, CV52 9QT.
gerald.finchley@tailoredgivingco.example
www.tailoredgivingco.example
In UK: 07831 604529
Global: +44 7831 604529

Font styles to use
Serif
Decorative

Requirements
Must have
• clean look (I used to like the Orbis Fund Business cards!). understated air of high quality. however I think that I like 'Tailored Giving...' rather than 'Tailored Giving Ltd.' because the former hints (I think at least) that you are on a journey leading to somewhere that can be great. whole aim of company is to get inside the clients hearts and enable them to achieve their personal dreams of helping people. Wife thinks a thumbprint or handprint somewhere might be good (I know what she means but I am not convinced)
Nice to have
• I would like the stationery to bear the words 'Tailored Giving...' the three dots signify that this is going to lead somewhere, something is going to happen. I am thinking about a strapline for the letterhead and folder: your experience - your heart - your legacy.
Should not have
• must not look like a business card from a charity or NGO.

```html
<!DOCTYPE html>
<html lang="en">
<head>
<meta charset="utf-8">
<title>Tailored Giving – Business Card</title>
<link rel="stylesheet" href="https://fonts.googleapis.com/css2?family=Cinzel:wght@400;700&display=swap">
<style>
  :root {
    --page-bg: #f3f4f3;
    --card-bg: #ffffff;
    --card-edge: #c9c9c9;
    --ink: #1f1f1f;
    --rule: #8f8f8f;
    --mark: #d9d9d9;
  }
  html, body {
    margin: 0;
    width: 1200px;
    height: 999px;
    overflow: hidden;
    background: var(--page-bg);
  }
  .card {
    position: absolute;
    left: 185px;
    top: 248px;
    width: 821px;
    height: 516px;
    background: var(--card-bg);
    border: 2px solid var(--card-edge);
    font-family: "Cinzel", "Times New Roman", serif;
    color: var(--ink);
  }
  .brand {
    position: absolute;
    left: 0;
    right: 0;
    top: 50px;
    display: flex;
    justify-content: center;
    align-items: center;
    gap: 16px;
    font-weight: 700;
    font-size: 46px;
    letter-spacing: 0.5px;
    line-height: 1;
  }
  .brand-square {
    width: 56px;
    height: 56px;
    background: var(--mark);
  }
  .divider {
    position: absolute;
    left: 38px;
    top: 148px;
    width: 750px;
    height: 12px;
  }
  .contact {
    position: absolute;
    left: 154px;
    top: 236px;
    line-height: 34px;
    font-size: 24px;
  }
  .contact-name {
    font-weight: 700;
  }
  .address {
    position: absolute;
    left: 0;
    width: 784px;
    top: 428px;
    text-align: center;
    font-size: 25px;
    line-height: 35px;
  }
</style>
</head>
<body>
  <div class="card">
    <div class="brand">
      <span>Tailored</span>
      <span class="brand-square" aria-hidden="true"></span>
      <span>Giving</span>
    </div>

    <svg class="divider" viewBox="0 0 750 12" aria-hidden="true">
      <polyline points="0,4 240,4 245,9 750,9" fill="none" stroke="var(--rule)" stroke-width="2"/>
    </svg>

    <div class="contact">
      <div class="contact-name">Alan Porter</div>
      <div class="contact-email">email@example.com</div>
      <div class="contact-phone">718-555-0192</div>
    </div>

    <div class="address">
      <div>17 Corlett Road,&nbsp; Ludmere-on-vane</div>
      <div>Warwickshire - CV52 9QT</div>
    </div>
  </div>
</body>
</html>
```